Webdesign für  Photovoltaikanlagen und E-Ladeinfrastruktur
Webdesign für Photovoltaikanlagen und E-Ladeinfrastruktur
Zielgruppe
Die VALMO Energy GmbH ist ein Spezialist für die Planung und Projektierung von Photovoltaikanlagen und E-Ladeinfrastruktur.
Aufgabenstellung
- Design-Tool: Adobe Photoshop
- Hinweis: Die Firma wird sich neue aufstellen, was das Leistungsangebot betrifft. Sie können sich deshalb nur bedingt an der derzeitigen Website orientieren, alle fremden Logos (wie z.b. ORUPA) dürfen nicht mehr genutzt werden
- Gern hätten wir einen 'frischen' Slogan im headerbild

```html
<!DOCTYPE html>
<html lang="de">
<head>
<meta charset="utf-8">
<title>VALMO Energy – Webdesign</title>
<link rel="stylesheet" href="https://fonts.googleapis.com/css2?family=Montserrat:wght@600;700;800&family=Arimo:wght@400;700&display=swap">
<style>
:root{
  --green:#067a4d;
  --green-dark:#05683f;
  --grey-bg:#e4e4e4;
  --stage:#d9d9d9;
  --text:#333;
  --white:#fff;
}
*{box-sizing:border-box;margin:0;padding:0}
html,body{width:1200px;height:1200px;overflow:hidden;background:var(--stage)}
.stage{width:1200px;height:1200px;position:relative}
.page{position:absolute;left:343px;top:0;width:827px;height:1932px;background:var(--white);
  transform:scale(.6211);transform-origin:0 0;font-family:"Arimo",Arial,sans-serif;color:var(--text)}
.abs{position:absolute}
.brand{font-family:"Montserrat",sans-serif;font-weight:800;color:var(--green);letter-spacing:1px}
.header{left:0;top:0;width:827px;height:68px}
.header .brand{left:35px;top:18px;font-size:26px}
.nav{right:32px;top:30px;display:flex;gap:17px;font-size:6.5px;text-transform:uppercase;letter-spacing:.2px;color:#222}
.hero-text{left:0;top:68px;width:413px;height:245px;background:var(--green)}
.hero-title{left:77px;top:66px;color:var(--white);font-family:"Montserrat",sans-serif;font-weight:700;font-size:16px;line-height:25px;text-transform:uppercase}
.btn-outline{border:2px solid var(--white);color:var(--white);border-radius:16px;font-family:"Montserrat",sans-serif;font-weight:700;text-transform:uppercase;display:flex;align-items:center;justify-content:center;letter-spacing:.6px}
.btn-fill{background:var(--green);color:var(--white);border-radius:16px;font-family:"Montserrat",sans-serif;font-weight:700;text-transform:uppercase;display:flex;align-items:center;justify-content:center;letter-spacing:1px}
.hero-btn{left:75px;top:159px;width:120px;height:30px;font-size:13px}
.hero-photo{left:413px;top:68px;width:414px;height:245px;background:radial-gradient(circle at 12% 25%,#fff 0,#eaf2fb 12%,transparent 30%),linear-gradient(135deg,#6f9fd8,#3a6ec2 55%,#2a58a8)}
.intro .brand{left:0;width:827px;top:352px;text-align:center;font-size:40px}
.intro-sub{left:0;width:827px;top:426px;text-align:center;font-family:"Montserrat",sans-serif;font-weight:700;font-size:8.5px;color:var(--green);text-transform:uppercase}
.intro-copy{left:207px;width:413px;top:444px;text-align:center;font-size:9px;line-height:11px}
.intro-copy p+p{margin-top:8px}
.intro-btn{left:345px;top:562px;width:138px;height:29px;font-size:12px}
.tile{top:622px;width:276px;height:184px}
.tile-band{left:0;top:805px;width:827px;height:54px;background:var(--green)}
.tile-btn{top:15px;height:25px;font-size:8.5px}
.news{left:0;top:859px;width:827px;height:472px;background:var(--grey-bg)}
.section-title{left:0;width:827px;text-align:center;font-family:"Montserrat",sans-serif;font-weight:700;font-size:12px;color:var(--green);letter-spacing:.8px;text-transform:uppercase}
.card{top:77px;width:161px;height:313px;background:var(--white)}
.card-img{height:107px}
.card-body{padding:17px 13px 0;font-size:8.8px;line-height:11px}
.card-body h3{font-size:9px;font-weight:700;color:#111;margin-bottom:8px}
.card-body .more{display:block;margin-top:8px;font-weight:700;color:var(--green)}
.news-btn{left:369px;top:420px;width:95px;height:23px;font-size:8.5px;border-radius:12px}
.field{left:207px;width:413px;border-bottom:1px solid var(--green);font-size:9px;color:var(--green);padding-left:15px}
.send-btn{left:508px;top:1656px;width:104px;height:28px;font-size:12px;border-radius:14px}
.map{left:0;top:1722px;width:827px;height:175px;background:linear-gradient(120deg,#eef0ee,#e6e9e4 60%,#eef0ea)}
.map-card{left:3px;top:3px;width:122px;height:37px;background:var(--white);box-shadow:0 1px 2px rgba(0,0,0,.2);padding:4px 6px;font-size:4.5px;line-height:6px;color:#444}
.map-card b{color:#111}
.map-card .link{color:#1a73e8}
.footer{left:0;top:1897px;width:827px;height:35px;background:var(--green);color:var(--white);font-size:6.5px;display:flex;align-items:center;gap:17px;padding-left:140px}
</style>
</head>
<body>
<div class="stage">
  <div class="page">
    <header class="abs header">
      <div class="abs brand">VALMO</div>
      <nav class="abs nav"><span>Unternehmen</span><span>E-Ladeinfrastruktur</span><span>Photovoltaik</span><span>Planung und Projektierung</span><span>Aktuelles</span><span>Kontakt</span></nav>
    </header>

    <section class="abs hero-text">
      <h1 class="abs hero-title">Ihr Spezialist für Anlagen<br>der regenerativen<br>Energieerzeugung</h1>
      <div class="abs btn-outline hero-btn">Kontakt</div>
    </section>
    <div class="abs hero-photo" role="img" aria-label="Solarmodule vor blauem Himmel mit Sonne"></div>

    <section class="intro">
      <div class="abs brand">VALMO</div>
      <h2 class="abs intro-sub">Lorem ipsum dolor sit amet consetetur sadipscing elitr</h2>
      <div class="abs intro-copy">
        <p>Lorem ipsum dolor sit amet, consetetur sadipscing elitr, sed diam nonumy eirmod tempor invidunt ut labore et dolore magna aliquyam erat, sed diam voluptua. At vero eos et accusam et justo duo dolores et ea rebum. Stet clita kasd gubergren, no sea takimata sanctus est Lorem ipsum dolor sit amet. Lorem ipsum dolor sit amet, consetetur sadipscing elitr, sed diam nonumy eirmod tempor invidunt ut labore et dolore magna aliquyam erat, sed diam voluptua.</p>
        <p>At vero eos et accusam et justo duo dolores et ea rebum. Stet clita kasd gubergren, no sea takimata sanctus est Lorem ipsum dolor sit amet...</p>
      </div>
      <div class="abs btn-fill intro-btn">Unternehmen</div>
    </section>

    <div class="abs tile" style="left:0;background:linear-gradient(180deg,#8fb6e0 0,#c9d9a0 45%,#a9b060 60%,#8c8f8f 100%)" role="img" aria-label="Elektroauto an einer Ladesäule"></div>
    <div class="abs tile" style="left:276px;background:linear-gradient(180deg,#9cc0e8 0,#c56a3e 45%,#eee 70%,#6f9a45 100%)" role="img" aria-label="Wohnhaus mit Solarmodulen auf dem Dach"></div>
    <div class="abs tile" style="left:552px;width:275px;background:linear-gradient(180deg,#5d7fb0,#3b5680 60%,#b48a70 100%)" role="img" aria-label="Hände halten eine junge Pflanze"></div>
    <div class="abs tile-band">
      <div class="abs btn-outline tile-btn" style="left:59px;width:159px">E-Ladeinfrastruktur</div>
      <div class="abs btn-outline tile-btn" style="left:355px;width:117px">Photovoltaik</div>
      <div class="abs btn-outline tile-btn" style="left:596px;width:186px">Planung und Projektierung</div>
    </div>

    <section class="abs news">
      <h2 class="abs section-title" style="top:40px">Aktuelles</h2>
      <article class="abs card" style="left:138px">
        <div class="card-img" style="background:linear-gradient(180deg,#7aa6d8,#cfe0ef 45%,#3e6f2c 70%,#2b4d1f)" role="img" aria-label="Windkraftanlage über Wald"></div>
        <div class="card-body"><h3>Beitrag Lorem Ipsum</h3>Lorem ipsum dolor sit amet, consetetur sadipscing elitr, sed diam nonumy eirmod tempor invidunt ut labore et dolore magna aliquyam erat, sed diam voluptua. At vero eos et accusam et justo duo dolores et ea rebum. Stet clita kasd gubergren, no sea takimata sanctus est Lorem ipsum dolor sit amet...<span class="more">mehr...</span></div>
      </article>
      <article class="abs card" style="left:333px">
        <div class="card-img" style="background:linear-gradient(135deg,#1d5f8a,#3aa58f 50%,#0f3b5c)" role="img" aria-label="Rohrleitungen einer Industrieanlage"></div>
        <div class="card-body"><h3>Beitrag Lorem Ipsum</h3>Lorem ipsum dolor sit amet, consetetur sadipscing elitr, sed diam nonumy eirmod tempor invidunt ut labore et dolore magna aliquyam erat, sed diam voluptua. At vero eos et accusam et justo duo dolores et ea rebum. Stet clita kasd gubergren, no sea takimata sanctus est Lorem ipsum dolor sit amet...<span class="more">mehr...</span></div>
      </article>
      <article class="abs card" style="left:528px">
        <div class="card-img" style="background:linear-gradient(135deg,#a0604a,#2b3b5c 45%,#1d2a44)" role="img" aria-label="Montage von Solarmodulen auf einem Dach"></div>
        <div class="card-body"><h3>Beitrag Lorem Ipsum</h3>Lorem ipsum dolor sit amet, consetetur sadipscing elitr, sed diam nonumy eirmod tempor invidunt ut labore et dolore magna aliquyam erat, sed diam voluptua. At vero eos et accusam et justo duo dolores et ea rebum. Stet clita kasd gubergren, no sea takimata sanctus est Lorem ipsum dolor sit amet...<span class="more">mehr...</span></div>
      </article>
      <div class="abs btn-fill news-btn">Siehe mehr</div>
    </section>

    <section class="contact">
      <h2 class="abs section-title" style="top:1375px">Kontaktformular</h2>
      <div class="abs field" style="top:1414px;height:16px">Name / Firma</div>
      <div class="abs field" style="top:1452px;height:18px">Telefon</div>
      <div class="abs field" style="top:1490px;height:19px">E-Mail</div>
      <div class="abs field" style="top:1528px;height:21px">Ansprechpartner</div>
      <div class="abs field" style="top:1567px;height:67px">Nachricht</div>
      <div class="abs btn-fill send-btn">Senden</div>
    </section>

    <div class="abs map" role="img" aria-label="Stadtplan mit Standortmarkierung">
      <div class="abs map-card"><b>Lindenweg 12</b><br>Lindenweg 12, 04109 Musterstadt<br><span class="link">Größere Karte ansehen</span></div>
      <svg class="abs" style="left:405px;top:70px" width="12" height="16" viewBox="0 0 12 16"><path d="M6 0a6 6 0 0 0-6 6c0 4.5 6 10 6 10s6-5.5 6-10a6 6 0 0 0-6-6z" fill="#e0463a"/><circle cx="6" cy="6" r="2.2" fill="#a8231a"/></svg>
    </div>

    <footer class="abs footer"><span>Impressum</span><span>Datenschutz</span></footer>
  </div>
</div>
</body>
</html>
```